Brevant Business Card

I have a business that is called "Brevant Electrical Products LTD" My company deals with top of the range laptops and mobile phones that are exclusive. I need a business card that will be eye catching but not over complicated.

Target Market(s)

Adults aged 19 to 50
Upper middle class

Industry/Entity Type

Business

Requirements
Must have
• Company name/logo (file attached)
• It must have my contact information which is:

• Name: Dale Marwick

• Position: Managing Director 

• Business Address: 7 Hapton Row, London, W4 9QD

• Contact Number: 02085193604
• Mobile: 07814260537
• Email: info@brevant-goods.co.uk
Nice to have
• Simple and stylish
• Eye catching

```html
<!DOCTYPE html>
<html lang="en">
<head>
<meta charset="utf-8">
<title>Brevant Electrical Products – Business Card</title>
<link rel="stylesheet" href="https://fonts.googleapis.com/css2?family=Arimo:wght@400&family=Playfair+Display:ital,wght@1,700&display=swap">
<style>
  :root {
    --stage: #ececec;
    --card-white: #ffffff;
    --brand-cyan: #1ba3d6;
    --title-blue: #7fa6c4;
    --rule-grey: #d9dfe4;
    --sky-light: #ffffff;
    --sky-deep: #bfe6f6;
    --photo-light: #f4f5f6;
    --photo-mid: #c9cdd1;
    --photo-dark: #6f757b;
  }
  * { box-sizing: border-box; margin: 0; padding: 0; }
  html, body {
    width: 1200px; height: 486px; overflow: hidden;
    background: var(--stage);
  }
  .sheet { position: relative; width: 1200px; height: 486px; }
  .card {
    position: absolute; top: 105px; width: 509px; height: 303px;
    overflow: hidden; box-shadow: 0 2px 8px rgba(0,0,0,.25);
  }
  .card--front { left: 97px; }
  .card--back {
    left: 630px;
    background: linear-gradient(180deg, var(--sky-light) 0%, var(--sky-light) 45%, var(--sky-deep) 100%);
    text-align: center;
    font-family: "Arimo", Arial, sans-serif;
    color: var(--brand-cyan);
  }
  .hero-photo {
    position: absolute; inset: 0;
    background:
      radial-gradient(ellipse at 78% 30%, var(--photo-dark) 0%, rgba(111,117,123,0) 28%),
      linear-gradient(160deg, var(--photo-mid) 0%, var(--photo-light) 45%, var(--photo-mid) 100%);
  }
  .brand-lockup {
    position: absolute; left: 0; right: 0; top: 118px;
    display: flex; align-items: center; justify-content: center; gap: 14px;
    font-family: "Arimo", Arial, sans-serif; color: var(--brand-cyan);
  }
  .brand-dot {
    width: 22px; height: 22px; border-radius: 50%;
    background: var(--brand-cyan); flex: none;
  }
  .brand-name { font-size: 30px; line-height: 1.15; letter-spacing: 1px; }
  .holder-name {
    position: absolute; left: 0; right: 0; top: 30px;
    font-size: 27px; letter-spacing: 1px; text-transform: uppercase;
  }
  .holder-rule {
    position: absolute; left: 125px; width: 256px; top: 68px;
    border-top: 1px solid var(--rule-grey);
  }
  .holder-title {
    position: absolute; left: 0; right: 0; top: 72px;
    font-family: "Playfair Display", Georgia, serif;
    font-style: italic; font-weight: 700; font-size: 15px;
    color: var(--title-blue); letter-spacing: .5px;
  }
  .contact-list {
    position: absolute; left: 0; right: 0; top: 203px;
    list-style: none; font-size: 17px; line-height: 21.5px;
  }
</style>
</head>
<body>
<main class="sheet">
  <section class="card card--front">
    <div class="hero-photo" role="img" aria-label="Photo of a laptop keyboard with a mobile phone resting on it"></div>
    <div class="brand-lockup">
      <span class="brand-dot"></span>
      <span class="brand-name">Brevant<br>Electrical Products</span>
    </div>
  </section>

  <section class="card card--back">
    <h1 class="holder-name">Dale Marwick</h1>
    <div class="holder-rule"></div>
    <p class="holder-title">Managing Director</p>
    <ul class="contact-list">
      <li>Business Address: 7 Hapton Row, London, W4 9QD</li>
      <li>Contact Number: 02085193604</li>
      <li>Mobile: 07814260537</li>
      <li>Email: info@brevant-goods.co.uk</li>
    </ul>
  </section>
</main>
</body>
</html>
```